Redesign of existing business card

I would like the "signage" attachment converted into a business card. This needs to be double sided aswell, keeping the phone number and names on the front, and the email + website on the back.

Second attachment is the current business card design.

Larger font for contact details is required.

Must keep to original color themes (electric blue, silver/grey etc)

Back of the card to have blue background with white writing.

Industry/Entity Type

Business

Contact Information for Business Card

Refer to existing design from attachments

Requirements
Must have
• Refer to existing design from attachments
Nice to have

```html
<!DOCTYPE html>
<html lang="en">
<head>
<meta charset="utf-8">
<title>Kestrel Electro Services – Business Card</title>
<link rel="stylesheet" href="https://fonts.googleapis.com/css2?family=Exo+2:wght@600;700&display=swap">
<style>
  :root {
    --electric-blue: #3a52a8;
    --electric-blue-deep: #2f4596;
    --silver: #9a9ca3;
    --card-white: #ffffff;
    --stage: #2a2a2c;
  }
  * { margin: 0; padding: 0; box-sizing: border-box; }
  html, body { width: 1200px; height: 1000px; overflow: hidden; }
  body {
    background: var(--stage);
    font-family: "Exo 2", sans-serif;
    position: relative;
  }
  .card {
    position: absolute;
    width: 600px;
    height: 345px;
    border-radius: 26px;
    overflow: hidden;
  }

  /* Back of card */
  .card-back {
    left: 120px;
    top: 110px;
    background: var(--electric-blue);
    color: var(--card-white);
  }
  .card-back .brand-mark {
    position: absolute;
    left: 48px;
    top: 62px;
    width: 220px;
    height: 220px;
    border: 22px solid var(--card-white);
    border-radius: 50%;
  }
  .card-back .brand-name {
    position: absolute;
    left: 300px;
    top: 80px;
    font-size: 30px;
    font-weight: 700;
    line-height: 1.15;
    letter-spacing: 1px;
    color: var(--card-white);
  }
  .card-back .web-details {
    position: absolute;
    right: 34px;
    bottom: 64px;
    text-align: right;
    list-style: none;
    font-size: 19px;
    font-weight: 700;
    line-height: 1.6;
  }

  /* Front of card */
  .card-front {
    left: 480px;
    top: 545px;
    background: var(--card-white);
  }
  .card-front .brand-row {
    position: absolute;
    left: 36px;
    top: 48px;
    display: flex;
    align-items: center;
    gap: 20px;
  }
  .card-front .brand-mark {
    width: 104px;
    height: 104px;
    flex: none;
    border: 12px solid var(--silver);
    border-radius: 50%;
  }
  .card-front .brand-name {
    font-size: 34px;
    font-weight: 700;
    line-height: 1.1;
    letter-spacing: 1px;
    color: var(--electric-blue);
  }
  .card-front .phone-band {
    position: absolute;
    left: 0;
    right: 0;
    top: 210px;
    height: 78px;
    background: var(--electric-blue);
    display: flex;
    align-items: center;
    gap: 18px;
    padding-left: 70px;
    color: var(--card-white);
  }
  .card-front .phone-icon { width: 30px; height: 30px; }
  .card-front .phone-number {
    font-size: 46px;
    font-weight: 600;
    letter-spacing: 3px;
  }
</style>
</head>
<body>
  <section class="card card-back" aria-label="Back of business card">
    <div class="brand-mark"></div>
    <p class="brand-name">KESTREL<br>ELECTRO SERVICES</p>
    <ul class="web-details">
      <li>www.kestrelelectro.com.au</li>
      <li>hello@kestrelelectro.com.au</li>
    </ul>
  </section>

  <section class="card card-front" aria-label="Front of business card">
    <div class="brand-row">
      <div class="brand-mark"></div>
      <p class="brand-name">KESTREL<br>ELECTRO SERVICES</p>
    </div>
    <div class="phone-band">
      <svg class="phone-icon" viewBox="0 0 24 24" aria-hidden="true">
        <path fill="#ffffff" d="M6.6 10.8a15.1 15.1 0 0 0 6.6 6.6l2.2-2.2a1 1 0 0 1 1-.25 11.4 11.4 0 0 0 3.6.57 1 1 0 0 1 1 1V20a1 1 0 0 1-1 1A17 17 0 0 1 3 4a1 1 0 0 1 1-1h3.5a1 1 0 0 1 1 1c0 1.25.2 2.45.57 3.6a1 1 0 0 1-.25 1z"/>
      </svg>
      <span class="phone-number">0491 570 110</span>
    </div>
  </section>
</body>
</html>
```